Theatre Poster Design/Key Art Project

I need key art that can be used in a variety of iterations to promote a theatrical production of Lucas Emory Finch’s adaptation of MARGIT SOLVANG by Osvald Kremer. This is a landmark work of drama that takes place in the very late 19th Century. For more information, consult http://en.lorevault-archive.org/wiki/Margit_Solvang

“Returning from their honeymoon, Anton and Margit Rydell begin to settle into their new life together. With the return of Sigurd Halvik, Anton’s academic nemesis, the couple’s relationship unravels amidst whispered secrets, professional disappointments, and a startling realization of what life truly holds for Margit as Anton’s wife. Passion and rivalries flare in this new adaptation by Lucas Emory Finch, who breathes new life into Kremer’s classic tale with an interpretation of Margit unlike any other.”

While the initial project is an 11"x17" poster, I need the essential design elements to be able to be replicated on a direct mail card, in email blitzes, etc.

This is a serious drama. We would like a highly graphic poster that does not attempt to tell the story.

Reason: We ran out of time and were unable to provide feedback. Things around here are very busy. We'd like to extend this contest to hopefully get a few more designs and provide feedback in the next day or two to those designs that we are considering as of now.

I want to try to get darker in terms of the design. Something that is going to be more compelling to our average patron. Can we play with the cleaning of the pistol.It is clear in the script that Margit loves her guns and would care greatly for them, so I want to play with the guns and the accessories that may go along with the guns of the period.

Target Market(s)

university students ages 18-22
theatre patrons ages 35-80

Industry/Entity Type

Work

Requirements
Must have
• must use the KPD Theatre logo
Should not have
• tragedy/comedy masks

```html
<!DOCTYPE html>
<html lang="en">
<head>
<meta charset="utf-8">
<title>Margit Solvang — KPD Theatre &amp; Dance</title>
<link rel="stylesheet" href="https://fonts.googleapis.com/css2?family=Crimson+Text:wght@400&display=swap">
<style>
  :root {
    --paper: #ffffff;
    --ink: #0b0b0b;
    --hair-mid: #1c1c1c;
    --hair-edge: #8a8a8a;
    --type-light: #ffffff;
    --brand-ink: #1a1a1a;
  }
  html, body {
    margin: 0;
    padding: 0;
    overflow: hidden;
    background: var(--paper);
  }
  .poster {
    position: relative;
    width: 775px;
    height: 1200px;
    overflow: hidden;
    background: var(--paper);
    font-family: "Crimson Text", Georgia, serif;
  }
  .key-art {
    position: absolute;
    inset: 0;
    width: 775px;
    height: 1200px;
  }
  .brand {
    position: absolute;
    top: 22px;
    right: 22px;
    text-align: right;
    color: var(--brand-ink);
    font-weight: 400;
    line-height: 1.05;
  }
  .brand__name {
    display: block;
    font-size: 36px;
    letter-spacing: 0.5px;
  }
  .brand__school {
    display: block;
    font-size: 16px;
    letter-spacing: 1.2px;
    text-transform: uppercase;
    margin-top: 4px;
  }
  .title {
    position: absolute;
    left: 80px;
    top: 708px;
    margin: 0;
    color: var(--type-light);
    font-weight: 400;
    font-size: 112px;
    line-height: 136px;
    letter-spacing: -1px;
  }
  .title span { display: block; }
  .credits {
    position: absolute;
    top: 994px;
    bottom: 0;
    display: block;
    margin: 0;
    padding: 0 0 0 8px;
    list-style: none;
    border-left: 1.5px solid var(--type-light);
    color: var(--type-light);
    font-size: 14.5px;
    line-height: 20px;
  }
  .credits li {
    display: block;
    margin: 0;
    padding: 0;
    white-space: nowrap;
  }
  .credits--author { left: 89px; width: 126px; }
  .credits--run { left: 223px; width: 160px; }
</style>
</head>
<body>
  <main class="poster">
    <svg class="key-art" viewBox="0 0 775 1200" role="img" aria-label="High-contrast black and white photograph of a woman's face in profile with long, wind-swept dark hair filling most of the poster">
      <defs>
        <linearGradient id="hair-tone" x1="0" y1="0" x2="1" y2="0.3">
          <stop offset="0" stop-color="#0b0b0b"/>
          <stop offset="0.6" stop-color="#1c1c1c"/>
          <stop offset="1" stop-color="#8a8a8a"/>
        </linearGradient>
      </defs>
      <path fill="url(#hair-tone)"
            d="M0 20 C80 10 200 30 300 70 C400 110 470 190 520 300
               C570 410 600 520 625 630 C650 740 680 860 700 960
               C720 1060 735 1140 745 1200 L0 1200 Z"/>
    </svg>

    <header class="brand">
      <span class="brand__name">KPD Theatre &amp; Dance</span>
      <span class="brand__school">Kestrel Point University</span>
    </header>

    <h1 class="title"><span>Margit</span><span>Solvang</span></h1>

    <ul class="credits credits--author">
      <li>by Osvald Kremer</li>
      <li>adapted by Lucas</li>
      <li>Emory Finch</li>
    </ul>

    <ul class="credits credits--run">
      <li>Two Weeks Only!</li>
      <li>April 12-22</li>
      <li>Alder Theatre</li>
      <li>Tickets $6-$14</li>
      <li>555-018-4420</li>
      <li>kpd.tixbox.com</li>
    </ul>
  </main>
</body>
</html>
```